Quill And Ferry Business Card

I need a business card designed around my logo (which was designed here on Sketch Forum!)

Target Market(s)

Professional Businesses

Industry/Entity Type

Business

Requirements
Must have
• Details that must be on the business card:

Renata Ovalle
Director
0491 253 608
renata@quillandferry.com.au
www.quillandferry.com.au
PO Box 4720 Brindle Vale Vic 3187

```html
<!DOCTYPE html>
<html lang="en">
<head>
<meta charset="utf-8">
<title>Quill And Ferry Business Card</title>
<link rel="stylesheet" href="https://fonts.googleapis.com/css2?family=Cinzel:wght@500&family=PT+Sans&display=swap">
<style>
  :root {
    --backdrop: #2b2b2b;
    --brand-red: #c91f26;
    --card-white: #ffffff;
    --ink: #1c1c1c;
    --band-white: #ffffff;
  }
  * { margin: 0; padding: 0; box-sizing: border-box; }
  html, body { width: 1200px; height: 900px; overflow: hidden; }
  body {
    background: var(--backdrop);
    position: relative;
    font-family: "PT Sans", Arial, sans-serif;
  }
  .card {
    position: absolute;
    width: 510px;
    height: 300px;
    border-radius: 28px;
    overflow: hidden;
    top: 300px;
  }
  .card-front { left: 60px; background: var(--brand-red); }
  .card-back { left: 630px; background: var(--card-white); }
  .accent-band { position: absolute; inset: 0; width: 100%; height: 100%; }

  .brand-name {
    font-family: "Cinzel", "Times New Roman", serif;
    font-weight: 500;
    letter-spacing: 0.5px;
    white-space: nowrap;
  }
  .brand-tagline {
    font-family: "PT Sans", Arial, sans-serif;
    text-transform: uppercase;
    letter-spacing: 3px;
    white-space: nowrap;
  }

  .front-lockup {
    position: absolute;
    left: 0;
    width: 420px;
    top: 118px;
    text-align: center;
    color: var(--card-white);
  }
  .front-lockup .brand-name { font-size: 34px; line-height: 1; }
  .front-lockup .brand-tagline { font-size: 14px; margin-top: 8px; }

  .back-lockup {
    position: absolute;
    left: 110px;
    top: 74px;
  }
  .back-lockup .brand-name { font-size: 27px; line-height: 1; color: var(--ink); }
  .back-lockup .brand-tagline { font-size: 12px; color: var(--brand-red); margin-top: 4px; }
  .brand-square {
    position: absolute;
    left: 70px;
    top: 80px;
    width: 26px;
    height: 26px;
    background: var(--brand-red);
  }

  .contact {
    position: absolute;
    left: 150px;
    top: 170px;
    color: var(--ink);
    font-size: 14.5px;
    line-height: 1.25;
  }
  .contact-name { color: var(--brand-red); font-size: 19px; letter-spacing: 0.5px; }
  .contact-role { font-size: 13px; margin-bottom: 12px; }
  .contact-address { margin-bottom: 10px; }
  .divider { color: var(--brand-red); margin: 0 3px; }
</style>
</head>
<body>
  <section class="card card-front" aria-label="Business card front">
    <svg class="accent-band" viewBox="0 0 510 300" aria-hidden="true">
      <polygon points="440,0 510,0 510,60" fill="var(--band-white)"/>
    </svg>
    <div class="front-lockup">
      <div class="brand-name">QUILL AND FERRY</div>
      <div class="brand-tagline">Ledgers Kept Simple</div>
    </div>
  </section>

  <section class="card card-back" aria-label="Business card back">
    <svg class="accent-band" viewBox="0 0 510 300" aria-hidden="true">
      <polygon points="0,230 0,300 70,300" fill="var(--brand-red)"/>
    </svg>
    <span class="brand-square" aria-hidden="true"></span>
    <div class="back-lockup">
      <div class="brand-name">QUILL AND FERRY</div>
      <div class="brand-tagline">Ledgers Kept Simple</div>
    </div>
    <div class="contact">
      <div class="contact-name">Renata Ovalle</div>
      <div class="contact-role">Director</div>
      <div class="contact-address">PO Box 4720 Brindle Vale Vic 3187</div>
      <div class="contact-line">0491 253 608<span class="divider">|</span>renata@quillandferry.com.au</div>
      <div class="contact-line">www.quillandferry.com.au</div>
    </div>
  </section>
</body>
</html>
```